We provide career management services supported by 6 tools designed to assist our members in managin

We have our site up and running but need to change the overall look and feel of the site, from the external pages to the internal customer facing pages. I need a site that will appeal to recent college grads as the primary target audience to customer in there 50's either trying to hold on to the job they have or trying to move on.

I would like to have 2 pages designed for this contest, the home page and the customer internal dashboard page. You can view the home page at www.jobvantora.com. I have taken two screen shots of the not completed Dashboard page, top and bottom.

The winner of this contest will be hired by us to design all remaining pages for the site including our tools.

Project Deadline Extended
Reason: We are revising the specifications for the requested designs in an attempt at better conveying what we are looking for. Most designs received so far have been a reiteration of what we currently have and realize this may be due to a lack of communication. We will have our new spec up on Tuesday.

Target Market(s)

Recent grads.

Industry/Entity Type

College

Requirements
Must have
• Overall must feel professional but have a bit of fun to it. Colors of the site should lend themselves to our logo. Please go to jobvantora.com and take a look at logo and existing pages.

```html
<!DOCTYPE html>
<html lang="en">
<head>
<meta charset="utf-8">
<title>Jobvantora – Home</title>
<link rel="stylesheet" href="https://fonts.googleapis.com/css2?family=Ubuntu:wght@400;500;700&family=Oswald:wght@500&display=swap">
<style>
  :root{
    --red:#c4161c;
    --red-dark:#a50f14;
    --orange:#f39a1e;
    --orange-light:#f7b133;
    --ink:#333;
    --grey-text:#555;
    --rule:#d8d8d8;
    --footer:#474747;
    --footer-text:#e8e8e8;
    --white:#fff;
  }
  *{box-sizing:border-box;margin:0;padding:0}
  html,body{width:880px;height:1200px;overflow:hidden;background:var(--white)}
  body{position:relative;font-family:Arial,Helvetica,sans-serif;color:var(--ink)}
  .abs{position:absolute}
  .heading-font{font-family:'Ubuntu',sans-serif}

  /* header */
  .brand{left:103px;top:22px;font-family:'Ubuntu',sans-serif;font-weight:700;font-size:34px;color:var(--red);letter-spacing:-0.5px}
  .account-btn{top:12px;height:20px;border:1px solid #d98a12;background:linear-gradient(#fbc34a,var(--orange));border-radius:2px;display:flex;align-items:center;font-family:'Ubuntu',sans-serif;font-weight:700;font-size:11px;color:var(--red-dark);padding-left:6px}
  .account-btn span.ico{margin-left:6px;width:18px;height:18px;background:var(--red);display:flex;align-items:center;justify-content:center}
  .btn-register{left:633px;width:73px}
  .btn-login{left:716px;width:61px}
  .phone{left:634px;top:46px;display:flex;align-items:center;gap:8px;font-family:'Ubuntu',sans-serif;font-size:18px;font-weight:500;color:var(--orange)}
  .phone-ico{width:25px;height:25px;border-radius:50%;background:var(--red);display:flex;align-items:center;justify-content:center}

  /* nav */
  .main-nav{left:103px;top:85px;width:674px;height:30px;display:flex;background:var(--red)}
  .main-nav a{display:flex;align-items:center;justify-content:center;color:var(--white);text-decoration:none;font-family:'Ubuntu',sans-serif;font-size:12px;border-right:1px solid #d84a4e}
  .main-nav a:last-child{border-right:0}
  .main-nav a.active{background:var(--orange)}

  /* hero */
  .hero{left:103px;top:123px;width:674px;height:274px;background:linear-gradient(110deg,#e9ecef 0%,#c9b8a3 45%,#e3d3c2 70%,#8a8f96 100%)}
  .hero-caption{left:0;bottom:0;width:100%;height:35px;background:rgba(40,40,40,.65);display:flex;align-items:center;padding-left:60px;font-family:'Ubuntu',sans-serif;font-size:20px;color:var(--white)}
  .hero-dots{right:14px;top:13px;display:flex;gap:4px}
  .hero-dots i{width:10px;height:10px;border-radius:50%;background:var(--orange)}
  .hero-dots i:first-child{background:var(--red)}

  .section-title{left:103px;width:674px;text-align:center;font-family:'Ubuntu',sans-serif;font-size:16px;font-weight:500;color:#222;padding-bottom:5px;border-bottom:1px solid var(--rule)}
  .section-title em{font-style:normal;color:var(--red)}
  .welcome-title{top:410px}
  .welcome-text{left:110px;top:436px;width:660px;text-align:center;font-size:10px;line-height:15.5px;color:var(--grey-text)}

  /* feature cards */
  .card{top:525px;width:211px;height:170px;background:var(--white);border-top:4px solid var(--red);box-shadow:0 1px 6px rgba(0,0,0,.18)}
  .card h3{position:absolute;left:9px;top:6px;font-family:'Ubuntu',sans-serif;font-weight:400;font-size:12.5px;line-height:14px;color:#333}
  .card .mark{position:absolute;right:13px;top:10px;width:14px;height:14px;background:var(--orange)}
  .card .photo{position:absolute;left:10px;top:44px;width:190px;height:80px;background:linear-gradient(120deg,#dfe3e8,#b5a898 55%,#7d8794)}
  .card p{position:absolute;left:15px;top:130px;width:185px;font-size:8px;line-height:11.5px;color:#444}
  .card .more{position:absolute;right:10px;bottom:-2px;font-size:8px;font-weight:700;color:#333}
  .arrow{top:590px}

  .wisdom-title{top:736px}
  .video{left:103px;top:772px;width:421px;height:217px;background:linear-gradient(110deg,#d6dbe0,#b8a999 45%,#d8cbbd 75%,#9ea3a8)}
  .play{left:183px;top:80px;width:55px;height:37px;border-radius:7px;background:linear-gradient(#c9262b,#8e0f12);display:flex;align-items:center;justify-content:center}
  .video-bar{left:0;bottom:0;width:100%;height:20px;background:#1b1b1b;border-top:3px solid #444;display:flex;align-items:center;font-size:7px;color:#ccc;padding-left:62px}
  .video-bar::before{content:"";position:absolute;left:0;top:-3px;width:32px;height:3px;background:var(--red)}

  .wisdom-copy{left:534px;top:771px;width:244px;font-size:8px;line-height:11px;color:#222}
  .wisdom-copy .lead{font-weight:700;margin-bottom:13px}
  .wisdom-copy ul{list-style:none;margin-top:10px}
  .wisdom-copy li{position:relative;padding-left:13px;margin-bottom:7px;color:#333;font-size:7.5px}
  .wisdom-copy li::before{content:"";position:absolute;left:1px;top:2px;width:6px;height:6px;background:var(--orange)}
  .survey-btn{left:547px;top:957px;width:121px;height:32px;background:var(--red);border:1px solid var(--red-dark);border-radius:3px;display:flex;align-items:center;justify-content:center;font-family:'Oswald',sans-serif;font-size:15px;color:var(--white);box-shadow:0 1px 3px rgba(0,0,0,.3)}

  /* footer */
  .footer-shape{left:0;top:950px}
  .footer-col{top:1084px}
  .footer-col h4{font-family:'Ubuntu',sans-serif;font-weight:500;font-size:13px;color:var(--white);padding-bottom:6px;border-bottom:1px solid #5e5e5e;margin-bottom:10px}
  .footer-col,.footer-col p,.footer-col li{font-size:8px;color:var(--footer-text);line-height:12.5px}
  .footer-col ul{list-style:none;padding-left:8px}
  .footer-col li{margin-bottom:1.5px}
  .footer-col li::before{content:"» ";font-size:7px}
  .divider{top:1090px;width:1px;height:95px;background:#5a5a5a}
  .email-field{margin-top:6px;width:135px;height:17px;background:var(--white);border:1px solid #ccc;color:#666;font-size:8px;padding:3px 9px}
  .subscribe{margin-top:6px;display:inline-block;background:#222;color:var(--white);font-weight:700;font-size:8px;padding:3px 6px;border:1px solid #666}
  .contact-row{display:flex;gap:8px;margin-bottom:6px}
  .contact-row svg{flex:none}
  .social{display:flex;gap:7px;justify-content:center;margin-top:4px}
  .social i{width:18px;height:18px;background:#5b7bb8;border-radius:2px}
</style>
</head>
<body>

<header>
  <div class="abs brand">Jobvantora</div>
  <div class="abs account-btn btn-register">Register<span class="ico"><svg width="10" height="10" viewBox="0 0 10 10"><circle cx="5" cy="3" r="2.3" fill="#fff"/><path d="M1 10c0-3 2-4.5 4-4.5S9 7 9 10z" fill="#fff"/></svg></span></div>
  <div class="abs account-btn btn-login">Login<span class="ico"><svg width="10" height="10" viewBox="0 0 10 10"><rect x="1.5" y="4.5" width="7" height="5" fill="#fff"/><path d="M3 4.5V3a2 2 0 014 0v1.5" stroke="#fff" fill="none" stroke-width="1.3"/></svg></span></div>
  <div class="abs phone"><span class="phone-ico"><svg width="14" height="14" viewBox="0 0 14 14"><path d="M3 1l2 3-1.3 1.3c.8 1.8 2.2 3.2 4 4L9 8l3 2-1.3 2.5C6 12 2 8 1.5 3.2z" fill="#fff"/></svg></span>713-555-0186</div>
</header>

<nav class="abs main-nav">
  <a class="active" style="width:100px">Home</a>
  <a style="width:178px">About Jobvantora</a>
  <a style="width:115px">Our Team</a>
  <a style="width:172px">Products &amp; Services</a>
  <a style="width:109px">Contact</a>
</nav>

<section class="abs hero" role="img" aria-label="Photo of a smiling career advisor meeting with a young couple reviewing documents">
  <div class="abs hero-caption">Jobvantora Can Give You The Tools to Succeed!</div>
  <div class="abs hero-dots" style="top:auto;bottom:12px"><i></i><i></i><i></i></div>
</section>

<h2 class="abs section-title welcome-title">Welcome To <em>Jobvantora</em></h2>
<p class="abs welcome-text">Lorem ipsum dolor sit amet, consectetuer adipiscing elit, sed diam nonummy nibh euismod tincidunt ut laoreet dolore magna aliquam erat volutpat. Utvn wisi enim ad minim veniam, quis nostrud exerci tation ullamcorper suscipit lobortis nisl ut aliquip ex ea commodo consequat. Duis aute vel eum iriureml dolor in hendrerit in vulputate velit esse molestie consequat, vel illum dolore eu feugiat nulla facilisis at vero eros et accumsan et iusto odio dignissim quil blandit praesent luptatum zzril delenit augue duis dolore te feugait nulla facilisi.</p>

<svg class="abs arrow" style="left:86px" width="14" height="26" viewBox="0 0 14 26"><path d="M12 2L3 13l9 11" stroke="#aaa" stroke-width="3" fill="none"/></svg>
<svg class="abs arrow" style="left:778px" width="14" height="26" viewBox="0 0 14 26"><path d="M2 2l9 11-9 11" stroke="#f39a1e" stroke-width="3" fill="none"/></svg>

<article class="abs card" style="left:110px">
  <h3>Access Expert,<br>Real-Time Advice</h3><span class="mark"></span>
  <div class="photo" role="img" aria-label="Photo of colleagues listening to an advisor"></div>
  <p>Having an insider by your side who can provide insight into what organizations are looking for ...</p>
  <span class="more">Read More »</span>
</article>
<article class="abs card" style="left:334px">
  <h3>Ace Your<br>Interviews</h3><span class="mark"></span>
  <div class="photo" role="img" aria-label="Photo of a job interview panel"></div>
  <p>The biggest mistake most people make? Answering questions for the first time at the interview!</p>
  <span class="more">Read More »</span>
</article>
<article class="abs card" style="left:560px">
  <h3>Find the Career That’s<br>Right for You</h3><span class="mark"></span>
  <div class="photo" role="img" aria-label="Photo of a professional woman on the phone in an office"></div>
  <p>Is your resume good enough? Are the right companies finding you? Do you have difficulty ...</p>
  <span class="more">Read More »</span>
</article>

<h2 class="abs section-title wisdom-title">Take A Sneak Peak At Our <em>VantoraWISDOM</em></h2>

<div class="abs video" role="img" aria-label="Video still of two professionals in conversation">
  <div class="abs play"><svg width="18" height="20" viewBox="0 0 18 20"><path d="M1 1l16 9-16 9z" fill="#fff"/></svg></div>
  <div class="abs video-bar">
    <svg class="abs" style="left:14px;top:5px" width="8" height="9"><rect width="3" height="9" fill="#ccc"/><rect x="5" width="3" height="9" fill="#ccc"/></svg>
    <svg class="abs" style="left:40px;top:5px" width="12" height="9"><path d="M0 3h3l4-3v9L3 6H0z" fill="#ccc"/></svg>
    00:08 / 10:12
    <svg class="abs" style="right:10px;top:5px" width="80" height="9"><rect x="0" y="2" width="9" height="5" fill="#aaa"/><circle cx="27" cy="4.5" r="4" fill="#aaa"/><circle cx="50" cy="4.5" r="4" fill="#aaa"/><path d="M70 0h-3v3M77 0h3v3M70 9h-3V6M77 9h3V6" stroke="#aaa" fill="none" transform="translate(-1 0)"/></svg>
  </div>
</div>

<div class="abs wisdom-copy">
  <p class="lead">Our insider experts share their wisdom and best practices to ensure that our members are successful in their career journey.</p>
  <p style="font-weight:700">Have you wondered about:</p>
  <ul>
    <li>What steps should an employee take to manage their own career?</li>
    <li>What things do you look for in a resume?</li>
    <li>how important are soft skills versus technical skills?</li>
    <li>What a new employee should expect from the first 30 days of a job?</li>
    <li>What characteristics do successful people have?</li>
    <li>Examples of human capital initiative</li>
  </ul>
</div>
<div class="abs survey-btn">TAKE OUR SURVEY!</div>

<svg class="abs footer-shape" width="880" height="250" viewBox="0 0 880 250">
  <path d="M0 55 Q420 160 880 10 L880 250 L0 250Z" fill="#f39a1e"/>
  <path d="M0 70 Q420 170 880 32 L880 250 L0 250Z" fill="#474747"/>
</svg>

<footer>
  <div class="abs footer-col" style="left:102px;width:114px">
    <h4>Quick Links</h4>
    <ul><li>Home</li><li>About Jobvantora</li><li>Our Team</li><li>Products &amp; Services</li><li>Contact</li></ul>
  </div>
  <div class="abs divider" style="left:237px"></div>
  <div class="abs footer-col" style="left:258px;width:137px">
    <h4>Newsletter</h4>
    <p style="padding-left:1px">Get the latest updates by entering your email address</p>
    <div class="email-field">Email Address</div>
    <span class="subscribe">Subscribe</span>
  </div>
  <div class="abs divider" style="left:419px"></div>
  <div class="abs footer-col" style="left:443px;width:158px">
    <h4>Contact Details</h4>
    <div class="contact-row"><svg width="9" height="13" viewBox="0 0 9 13"><path d="M4.5 0A4.5 4.5 0 000 4.5C0 8 4.5 13 4.5 13S9 8 9 4.5A4.5 4.5 0 004.5 0z" fill="#fff"/><circle cx="4.5" cy="4.5" r="1.7" fill="#474747"/></svg><p>Lorem ipsum dolor sit consectetur adipiscing elit,site amet</p></div>
    <div class="contact-row"><svg width="10" height="10" viewBox="0 0 14 14"><path d="M3 1l2 3-1.3 1.3c.8 1.8 2.2 3.2 4 4L9 8l3 2-1.3 2.5C6 12 2 8 1.5 3.2z" fill="#fff"/></svg><p>(713) 555-0186</p></div>
    <div class="contact-row"><svg width="12" height="9" viewBox="0 0 12 9"><rect x=".5" y=".5" width="11" height="8" fill="none" stroke="#fff"/><path d="M.5.5l5.5 4.5L11.5.5" fill="none" stroke="#fff"/></svg><p>info@jobvantora.com</p></div>
  </div>
  <div class="abs divider" style="left:624px"></div>
  <div class="abs footer-col" style="left:650px;width:127px">
    <h4>Follow Us</h4>
    <div class="social"><i></i><i style="background:#3aa6dc"></i><i style="background:#2a7ab8"></i><i style="background:#d8332a"></i></div>
    <p style="text-align:center;margin-top:21px">Copyright © 2013. Jobvantora.<br>All rights reserved.</p>
  </div>
</footer>

</body>
</html>
```